Print materials for 3-star hotel

We are changing up our print materials (notepads, letterheads, key card jackets, small flyer for the room rates) We are a 3 star business hotel in the Philippines and have mainly used grey tones and clean, simple lines. See attached photos for logo and hotel interior photos.

Target Market(s)

Business

Contact Information for Business Card

Tamarind Crest Hotel
Governor Lualhati Avenue corner Pindang St Cebu City 6000 Philippines
Tel: +63 32 480 5273
Mobile: +63 917 608 4926
www.tamarindcresthotel.example

Font styles to use
Serif
Sans Serif

Requirements
Must have
• Simple
• Readable font and font size
Nice to have
• Neutral colors, grey and taupes
Should not have
• No purples and bright blues

```html
<!DOCTYPE html>
<html lang="en">
<head>
<meta charset="utf-8">
<title>Tamarind Crest Hotel — Stationery Set</title>
<link rel="stylesheet" href="https://fonts.googleapis.com/css2?family=Cormorant+Garamond:wght@500&family=Open+Sans:wght@400;600&display=swap">
<style>
  :root{
    --backdrop:#c4c4c4;
    --paper:#ffffff;
    --taupe:#6e6664;
    --slate:#737b80;
    --mark-light:#d6d2d0;
    --mark-dark:#6e6664;
    --ink:#5e5856;
    --shadow:0 6px 18px rgba(0,0,0,.18);
  }
  *{box-sizing:border-box;margin:0;padding:0}
  html,body{width:1200px;height:1200px;overflow:hidden}
  body{background:var(--backdrop);position:relative;font-family:"Open Sans",sans-serif}
  .piece{position:absolute;box-shadow:var(--shadow)}
  .brand{display:flex;flex-direction:column;align-items:center;gap:4px;font-family:"Cormorant Garamond",serif;font-weight:500;text-transform:uppercase;text-align:center;white-space:nowrap}
  .brand__square{width:18px;height:18px}
  .brand__name{letter-spacing:.22em;line-height:1}
  .brand__sub{letter-spacing:.5em;line-height:1}
  .brand--light{color:var(--mark-light)}
  .brand--light .brand__square{background:var(--mark-light)}
  .brand--dark{color:var(--mark-dark)}
  .brand--dark .brand__square{background:var(--mark-dark)}

  /* Letterhead */
  .letterhead{left:60px;top:150px;width:380px;height:537px;background:var(--paper)}
  .letterhead .brand{position:absolute;left:26px;top:30px}
  .letterhead .brand__square{width:14px;height:14px}
  .letterhead .brand__name{font-size:9px;letter-spacing:.18em}
  .letterhead .brand__sub{font-size:6px;letter-spacing:.45em}
  .letterhead__contact{position:absolute;top:38px;right:22px;display:flex;gap:12px;font-size:6px;line-height:1.7;color:var(--ink)}
  .letterhead__contact p{white-space:nowrap}

  /* Folder */
  .folder{left:480px;top:150px;width:380px;height:537px;background:var(--taupe)}
  .folder .brand{position:absolute;right:30px;top:150px}
  .folder .brand__name{font-size:13px}
  .folder .brand__sub{font-size:8px}

  /* Business cards */
  .card{width:250px;height:143px;left:900px}
  .card--front{top:150px;background:var(--taupe);display:flex;align-items:center;justify-content:center}
  .card--front .brand__name{font-size:11px}
  .card--front .brand__sub{font-size:7px}
  .card--back{top:320px;background:var(--slate);color:#eceeef;padding:22px 24px}
  .card__name{font-family:"Cormorant Garamond",serif;font-size:17px;letter-spacing:.12em;text-transform:uppercase;text-align:right}
  .card__role{font-size:8px;text-align:right;letter-spacing:.08em;margin-bottom:12px;opacity:.85}
  .card__line{display:flex;align-items:center;gap:7px;font-size:8px;line-height:1.9;white-space:nowrap}
  .card__line svg{width:9px;height:9px;flex:none}

  /* Rate cards */
  .rate{top:730px;width:520px;height:260px;display:flex;align-items:center;justify-content:center}
  .rate--taupe{left:60px;background:var(--taupe)}
  .rate--slate{left:620px;background:var(--slate)}
  .rate .brand__square{width:26px;height:26px}
  .rate .brand__name{font-size:20px}
  .rate .brand__sub{font-size:10px}
</style>
</head>
<body>

<section class="piece letterhead" aria-label="Letterhead">
  <div class="brand brand--dark">
    <span class="brand__square"></span>
    <span class="brand__name">Tamarind Crest</span>
    <span class="brand__sub">Hotel</span>
  </div>
  <div class="letterhead__contact">
    <div>
      <p>T +63 32 480 5273</p>
      <p>M +63 917 608 4926</p>
      <p>E stay@tamarindcresthotel.example</p>
    </div>
    <div>
      <p>Governor Lualhati Avenue</p>
      <p>corner Pindang St</p>
      <p>Cebu City 6000 Philippines</p>
    </div>
  </div>
</section>

<section class="piece folder" aria-label="Presentation folder">
  <div class="brand brand--light">
    <span class="brand__square"></span>
    <span class="brand__name">Tamarind Crest</span>
    <span class="brand__sub">Hotel</span>
  </div>
</section>

<section class="piece card card--front" aria-label="Business card front">
  <div class="brand brand--light">
    <span class="brand__square"></span>
    <span class="brand__name">Tamarind Crest</span>
    <span class="brand__sub">Hotel</span>
  </div>
</section>

<section class="piece card card--back" aria-label="Business card back">
  <p class="card__name">Rafael D</p>
  <p class="card__role">Front Office Manager</p>
  <p class="card__line"><svg viewBox="0 0 10 10"><path d="M2 1h2l1 2-1 1a5 5 0 0 0 2 2l1-1 2 1v2a1 1 0 0 1-1 1A8 8 0 0 1 1 2a1 1 0 0 1 1-1z" fill="#eceeef"/></svg>+63 32 480 5273 · +63 917 608 4926</p>
  <p class="card__line"><svg viewBox="0 0 10 10"><path d="M5 0a3.5 3.5 0 0 0-3.5 3.5C1.5 6 5 10 5 10s3.5-4 3.5-6.5A3.5 3.5 0 0 0 5 0zm0 5a1.5 1.5 0 1 1 0-3 1.5 1.5 0 0 1 0 3z" fill="#eceeef"/></svg>Governor Lualhati Ave cor Pindang St, Cebu City</p>
  <p class="card__line"><svg viewBox="0 0 10 10"><circle cx="5" cy="5" r="4" fill="none" stroke="#eceeef"/><path d="M1 5h8M5 1c-2 2-2 6 0 8M5 1c2 2 2 6 0 8" fill="none" stroke="#eceeef" stroke-width=".8"/></svg>www.tamarindcresthotel.example</p>
</section>

<section class="piece rate rate--taupe" aria-label="Room rate card">
  <div class="brand brand--light">
    <span class="brand__square"></span>
    <span class="brand__name">Tamarind Crest</span>
    <span class="brand__sub">Hotel</span>
  </div>
</section>

<section class="piece rate rate--slate" aria-label="Key card jacket">
  <div class="brand brand--light">
    <span class="brand__square"></span>
    <span class="brand__name">Tamarind Crest</span>
    <span class="brand__sub">Hotel</span>
  </div>
</section>

</body>
</html>
```